Business Card Design

I have two logos , one is for the front of the card and the other for the back. The front image is the road and the sun, the back image should be the atom with the motto at the bottom. The back of the card should be black with the atom and lettering white. The front should have the image with the road and lettering black with the yellow sun all on a white background.
Updates

I have changed what I would like done. The only logo I want to use is the atom logo. White lettering with a black background on the front and back of the card. There should be no contact info on the back of the card. On the back there should b the logo with company name and the slogan underneath at the bottom of the card, also on the back if you can have the logo  image in the background as well in a gray or silver can be tiled or cascade of some sort.

On the front it should have all of the contact info with an email address added  tarnvista@quellmail.net   Black background with white lettering and another larger image of the logo in a gray or silver in the background. The logo and name side by side with the slogan directly under the name.

Industry/Entity Type

Business

Contact Information for Business Card

Colin Marsh
Director of Operations
8162 Pemberly Ln #417
Millbrook, TX 78215
Cell: (512)804-3176
Fax: (512)471-0852

```html
<!DOCTYPE html>
<html lang="en">
<head>
<meta charset="utf-8">
<title>Bluebonnet Mobile Imaging — Business Card</title>
<link rel="stylesheet" href="https://fonts.googleapis.com/css2?family=Questrial&display=swap">
<style>
  :root {
    --page: #ececec;
    --card: #000000;
    --ink: #ffffff;
    --silver-soft: #262626;
    --silver-faint: #151515;
    --shadow: rgba(0, 0, 0, 0.28);
  }
  * { box-sizing: border-box; margin: 0; padding: 0; }
  html, body { width: 1200px; height: 849px; overflow: hidden; }
  body {
    background: var(--page);
    font-family: "Questrial", "Century Gothic", sans-serif;
    color: var(--ink);
  }
  .canvas { position: relative; width: 1200px; height: 849px; }
  .card {
    position: absolute;
    top: 275px;
    width: 520px;
    height: 300px;
    background: var(--card);
    overflow: hidden;
    box-shadow: 0 6px 14px var(--shadow);
  }
  .card--front { left: 50px; }
  .card--back  { left: 630px; }

  /* front */
  .front-mark-bg {
    position: absolute;
    left: 260px; top: 20px;
    width: 230px; height: 250px;
    border-radius: 50%;
    background: radial-gradient(ellipse at center, var(--silver-soft) 0%, var(--silver-faint) 55%, var(--card) 75%);
  }
  .brand { position: absolute; display: flex; align-items: center; }
  .brand__dot { border-radius: 50%; background: var(--ink); flex: none; }
  .brand__name { line-height: 1.1; white-space: nowrap; }
  .brand__slogan { line-height: 1.2; white-space: nowrap; }
  .card--front .brand { left: 30px; top: 36px; gap: 14px; }
  .card--front .brand__dot { width: 16px; height: 16px; }
  .card--front .brand__name { font-size: 19px; }
  .card--front .brand__slogan { font-size: 12.5px; margin-top: 3px; }

  .person {
    position: absolute; left: 0; right: 0; top: 143px;
    text-align: center;
  }
  .person__name { font-size: 18px; letter-spacing: 0.5px; }
  .person__title { font-size: 14px; margin-top: 4px; }

  .contact {
    position: absolute; left: 0; right: 0; top: 225px;
    text-align: center; font-size: 15px; line-height: 22px;
  }

  /* back */
  .back-pattern {
    position: absolute; inset: 0;
    background: linear-gradient(135deg, var(--silver-faint), #1b1b1b 50%, var(--silver-faint));
  }
  .card--back .brand { left: 40px; top: 150px; gap: 20px; }
  .card--back .brand__dot { width: 22px; height: 22px; }
  .card--back .brand__name { font-size: 29px; }
  .card--back .brand__slogan { font-size: 17.5px; margin-top: 4px; }
</style>
</head>
<body>
<main class="canvas">

  <section class="card card--front" aria-label="Card front">
    <div class="front-mark-bg" role="img" aria-label="Large faint silver company symbol in the background"></div>
    <div class="brand">
      <span class="brand__dot"></span>
      <div>
        <div class="brand__name">Bluebonnet Mobile Imaging</div>
        <div class="brand__slogan">Dependable Prompt Precise Care</div>
      </div>
    </div>
    <div class="person">
      <div class="person__name">COLIN MARSH</div>
      <div class="person__title">Director of Operations</div>
    </div>
    <div class="contact">
      <div>8162 Pemberly Ln #417 Millbrook, TX 78215</div>
      <div>Cell: (512)804-3176 Fax: (512)471-0852</div>
      <div>tarnvista@quellmail.net</div>
    </div>
  </section>

  <section class="card card--back" aria-label="Card back">
    <div class="back-pattern" role="img" aria-label="Tiled grey pattern of the company symbol"></div>
    <div class="brand">
      <span class="brand__dot"></span>
      <div>
        <div class="brand__name">Bluebonnet Mobile Imaging</div>
        <div class="brand__slogan">Dependable Prompt Precise Care</div>
      </div>
    </div>
  </section>

</main>
</body>
</html>
```